Homebuilder & Remodeling Firm looking for archectrual looking website

We are a Custom home building & remodeling company since 1986 and would like to launch a website.Carl Tondevik the principle of the firm is a graduate of Harwell Univesity school of architecture and draws his own designs and working drawings. and has done many residential, single and multi family projects in the Dallas Ft Worth Metroplex. We want our website to be architectural in design and visually appealing. We will eventually have photos to provide for you. The message we want to communicate is we have current update knowledge with trends, and longevity in experience. Our message is that we are a firm that designs and remodels fully through and we provide a well executed custom home that is unique to each client. The Homes that we build are unique ,authentic and sustainable architectural styles such as mid century modern, contemporary, transitional and they are sophisticated homes to compliment individual lifestyles of our clients. We have a passion for construction and an attention to detail that makes your dreams come to life. We listen to each clients every need in functionality and form and take them from pre-construction to post-construction follow -up.
We help you invest in your home. Thoughts Create Reality

EXAMPLES OF WEBSITES THAT WE LIKE. PLEASE DO
MORE CONTEMPORARY, SLEEK, ARCHITECTURAL

* Please make the LOGO a bigger part of design

http://pellamcrew.build/
https://www.vintrasol.co/
http://dostavanehomes.com/
http://www.milesfardowdesign.com/
http://www.quillmerton.com/
http://fennikdesignstudios.com/about
http://brandelorgc.com/

thank you,

Reason: We have many clients asking to see our website and re ready to launch something for them to look at

Target Market(s)

Home owners, home buyers, interior designers, All ages

Industry/Entity Type

Builders

Coding

Coded - Design and coding required

Number of Pages Required

5+ page

Font styles to use
Sans Serif

Requirements
Must have
• HTML5 OR PHP
• graphic artist must speak English:
• *Visually appealing, user friendly,
• * the website should reflect the stability and integrity of the company since it has been in business for over 30 years
• * a sophistication and refinement is our mandate.
Should not have
• Too busy, too much going on, we want more minimal in design and artsitic

```html
<!DOCTYPE html>
<html lang="en">
<head>
<meta charset="utf-8">
<title>Tondevik Builders — Projects</title>
<link href="https://fonts.googleapis.com/css2?family=Poppins:wght@400;500;600&display=swap" rel="stylesheet">
<style>
:root{
  --ink:#111;
  --muted:#8a8a8a;
  --accent:#c9dd1f;
  --navy:#1f2a4d;
  --paper:#fff;
  --rule:#e6e6e6;
}
*{box-sizing:border-box;margin:0;padding:0}
html,body{width:975px;height:1200px;overflow:hidden;background:var(--paper)}
body{position:relative;font-family:'Poppins',sans-serif;color:var(--ink)}
a{color:inherit;text-decoration:none}

.site-header{position:absolute;top:0;left:0;width:975px;height:60px}
.brand{position:absolute;left:29px;top:17px;display:flex;align-items:center;gap:8px}
.brand-mark{width:16px;height:16px;background:var(--navy)}
.brand-name{font-size:10px;font-weight:500;color:var(--ink);line-height:1}
.call{position:absolute;left:510px;top:21px;font-size:7px;color:var(--muted);letter-spacing:.5px}
.call b{color:var(--ink);font-weight:600;font-size:8px;letter-spacing:.3px}
.divider{position:absolute;left:659px;top:13px;width:1px;height:23px;background:var(--rule)}
.social{position:absolute;display:flex;gap:14px;align-items:center}
.social span{width:8px;height:8px;border-radius:50%;background:var(--ink)}
.social span:first-child{background:var(--accent)}
.header-social{left:686px;top:21px}
.menu{position:absolute;left:904px;top:20px;font-size:7px;font-weight:600;letter-spacing:.5px;display:flex;align-items:center;gap:6px}
.menu svg{display:block}

.intro{position:absolute;left:190px;top:165px;font-size:25.5px;font-weight:500;line-height:30px;letter-spacing:-.2px}

.filters{position:absolute;left:190px;top:324px;display:flex;gap:30px;font-size:9px;font-weight:500}
.filters .active{color:var(--accent)}

.grid{position:absolute;left:30px;top:380px;display:grid;grid-template-columns:repeat(4,217px);grid-auto-rows:292px;column-gap:15.5px;row-gap:16px}
.card{position:relative;overflow:hidden;color:#fff}
.card .photo{position:absolute;inset:0}
.card .title{position:absolute;left:21px;top:198px;font-size:15.5px;font-weight:600;line-height:18.5px;letter-spacing:-.3px}
.card .more{position:absolute;left:21px;top:263px;font-size:7.5px;font-weight:600;display:flex;align-items:center;gap:6px}
.card.featured{background:var(--accent);color:var(--ink)}
.card.featured .title{top:34px}
.card.featured p{position:absolute;left:21px;top:118px;width:178px;font-size:7px;line-height:12px;color:#3a4200}

.p1{background:linear-gradient(180deg,#e9ecef 0%,#cfd3d6 50%,#2a2b2d 78%,#0f1012 100%)}
.p3{background:linear-gradient(160deg,#b7c5d8 0%,#8d5c45 38%,#c9c2b6 60%,#3a3d3a 100%)}
.p4{background:linear-gradient(170deg,#b3a48a 0%,#6fa2c9 35%,#3d6f93 60%,#2c2c2e 100%)}
.p5{background:linear-gradient(180deg,#8d93a4 0%,#50535e 40%,#2f2c2b 70%,#1c1d1f 100%)}
.p6{background:linear-gradient(180deg,#c4c8cb 0%,#9ca2a6 45%,#4a4e4b 75%,#2c302d 100%)}
.p7{background:linear-gradient(180deg,#6a84a8 0%,#3e5470 40%,#6c6a63 65%,#232a36 100%)}
.p8{background:linear-gradient(160deg,#5b4a40 0%,#8a7a6c 45%,#4d5a4f 75%,#2a2f2c 100%)}

.site-footer{position:absolute;left:0;top:1058px;width:975px;font-size:7.2px;line-height:12.2px}
.site-footer .col{position:absolute;top:0}
.copy{left:190px}
.links-a{left:393px}
.links-a .active{color:var(--accent)}
.links-b{left:596px}
.lang{left:745px;display:flex;gap:6px;align-items:center}
.footer-social{left:837px;top:2px}
</style>
</head>
<body>
<header class="site-header">
  <a class="brand" href="#">
    <span class="brand-mark"></span>
    <span class="brand-name">Tondevik Builders</span>
  </a>
  <div class="call">CALL US: <b>(+080) 5521 74 30 216</b></div>
  <div class="divider"></div>
  <nav class="social header-social" aria-label="Social links"><span></span><span></span><span></span><span></span><span></span></nav>
  <a class="menu" href="#">MENU
    <svg width="10" height="8" viewBox="0 0 10 8"><path d="M0 .5h10M0 4h10M0 7.5h10" stroke="#111" stroke-width="1"/></svg>
  </a>
</header>

<h1 class="intro">Architecture Is A Visual Art<br>And The Building Speak For Themeselves</h1>

<nav class="filters">
  <a class="active" href="#">All</a>
  <a href="#">Building</a>
  <a href="#">Interior &amp; Exterior</a>
</nav>

<main class="grid">
  <article class="card">
    <div class="photo p1" role="img" aria-label="Angular concrete house beside a lake with mountains behind"></div>
    <h2 class="title">Triangle<br>Concrete House<br>On Lake</h2>
    <a class="more" href="#">See project <svg width="5" height="8" viewBox="0 0 5 8"><path d="M1 1l3 3-3 3" fill="none" stroke="currentColor"/></svg></a>
  </article>
  <article class="card featured">
    <h2 class="title">Ocean<br>Museum<br>Italy</h2>
    <p>Lorem ipsum dolor sit amet, consectetur adipil pcing elit. Proin nunc leo, rhoncus sit amet tolil arcu vel, pharetra volutpat sem lorn Donec tincidunt velit nec laoreet semper. Morbi tulor egestas imperdiet tortor, eget imperdiet ligula porta necPellentesque at tellus at sapien suscipit vulputate...</p>
    <a class="more" href="#">See project <svg width="5" height="8" viewBox="0 0 5 8"><path d="M1 1l3 3-3 3" fill="none" stroke="currentColor"/></svg></a>
  </article>
  <article class="card">
    <div class="photo p3" role="img" aria-label="Modern co-working building with wood cladding and a paved entry"></div>
    <h2 class="title">Milko<br>Co-Working<br>Building</h2>
    <a class="more" href="#">See project <svg width="5" height="8" viewBox="0 0 5 8"><path d="M1 1l3 3-3 3" fill="none" stroke="currentColor"/></svg></a>
  </article>
  <article class="card">
    <div class="photo p4" role="img" aria-label="Villa interior with large windows looking over a mountain lake"></div>
    <h2 class="title">Redesign<br>Interior For<br>Villa</h2>
    <a class="more" href="#">See project <svg width="5" height="8" viewBox="0 0 5 8"><path d="M1 1l3 3-3 3" fill="none" stroke="currentColor"/></svg></a>
  </article>
  <article class="card">
    <div class="photo p5" role="img" aria-label="Low horizontal wooden villa at dusk with cypress trees and a pool"></div>
    <h2 class="title">Wooden<br>Hozirontal<br>Villa</h2>
    <a class="more" href="#">See project <svg width="5" height="8" viewBox="0 0 5 8"><path d="M1 1l3 3-3 3" fill="none" stroke="currentColor"/></svg></a>
  </article>
  <article class="card">
    <div class="photo p6" role="img" aria-label="Small white gabled house with wooden slats under a cloudy sky"></div>
    <h2 class="title">Small<br>House Near<br>Wroclaw</h2>
    <a class="more" href="#">See project <svg width="5" height="8" viewBox="0 0 5 8"><path d="M1 1l3 3-3 3" fill="none" stroke="currentColor"/></svg></a>
  </article>
  <article class="card">
    <div class="photo p7" role="img" aria-label="Glass-fronted holiday residence lit at dusk above an indoor pool"></div>
    <h2 class="title">Bellecomde<br>Holiday<br>Residence</h2>
    <a class="more" href="#">See project <svg width="5" height="8" viewBox="0 0 5 8"><path d="M1 1l3 3-3 3" fill="none" stroke="currentColor"/></svg></a>
  </article>
  <article class="card">
    <div class="photo p8" role="img" aria-label="Cubic brick museum with a cantilevered glass volume over water"></div>
    <h2 class="title">Cubic<br>Inter Mesuem<br>In Rome</h2>
    <a class="more" href="#">See project <svg width="5" height="8" viewBox="0 0 5 8"><path d="M1 1l3 3-3 3" fill="none" stroke="currentColor"/></svg></a>
  </article>
</main>

<footer class="site-footer">
  <div class="col copy">© Vintrasol 2017<br>All Rights Resevered</div>
  <div class="col links-a"><a class="active" href="#">Site Map</a><br><a href="#">Term &amp; Conditions</a><br><a href="#">Privacy Policy</a><br><a href="#">Help</a><br><a href="#">Affiliate</a></div>
  <div class="col links-b"><a href="#">Our Location</a><br><a href="#">Career</a><br><a href="#">About</a><br><a href="#">Contact</a></div>
  <div class="col lang">English <svg width="8" height="5" viewBox="0 0 8 5"><path d="M.5.5l3.5 3.5 3.5-3.5" fill="none" stroke="#999"/></svg></div>
  <nav class="col social footer-social" aria-label="Social links"><span></span><span></span><span></span><span></span><span></span></nav>
</footer>
</body>
</html>
```